RW Business Card Design

My company provides advising/training and coaching services to business owners who want better financial results and better work/life balance. We help them through creating custom plans supported with education, strategic thinking and accountability.

We also help through some online courses which are geared to smaller businesses.
Updates

please also include our nth american contact # +1 555 208 4471

Industry/Entity Type

Financial

Contact Information for Business Card

Morgan Halberd
morgan@morganhalberd-example.com
+61 400 555 917
www.morganhalberd-example.com

```html
<!DOCTYPE html>
<html lang="en">
<head>
<meta charset="utf-8">
<title>RW Business Card Design</title>
<link rel="stylesheet" href="https://fonts.googleapis.com/css2?family=Montserrat:wght@300;400;600&display=swap">
<style>
  :root {
    --page-bg: #ecebe8;
    --card-bg: #ffffff;
    --brand-blue: #1d6fb8;
    --brand-grey: #8e8e93;
    --text-dark: #3a3a3c;
    --faint-blue: #d5e5f4;
    --faint-grey: #ececec;
    --icon-grey: #6a6a6e;
  }
  * { box-sizing: border-box; margin: 0; padding: 0; }
  html, body {
    width: 1200px;
    height: 918px;
    overflow: hidden;
    background: var(--page-bg);
    font-family: "Montserrat", Arial, sans-serif;
  }
  .canvas {
    width: 1200px;
    height: 918px;
    display: flex;
    align-items: center;
    justify-content: center;
    gap: 60px;
  }
  .card {
    position: relative;
    width: 540px;
    height: 310px;
    background: var(--card-bg);
    box-shadow: 0 6px 18px rgba(0,0,0,0.12);
    overflow: hidden;
  }

  /* Back side: centred name */
  .card-back {
    display: flex;
    align-items: center;
    justify-content: center;
    gap: 14px;
  }
  .brand-dot {
    width: 22px;
    height: 22px;
    border-radius: 50%;
    background: var(--brand-blue);
    flex: none;
  }
  .card-back .brand-name {
    font-size: 26px;
    font-weight: 600;
    letter-spacing: 1px;
    color: var(--brand-blue);
    text-transform: uppercase;
  }

  /* Front side: contact details */
  .card-front .brand {
    position: absolute;
    left: 34px;
    top: 48px;
    display: flex;
    align-items: center;
    gap: 10px;
  }
  .card-front .brand-dot { width: 16px; height: 16px; }
  .card-front .brand-name {
    font-size: 21px;
    font-weight: 600;
    letter-spacing: 0.5px;
    color: var(--brand-blue);
    text-transform: uppercase;
  }
  .faint-disc {
    position: absolute;
    right: -40px;
    bottom: -50px;
    width: 250px;
    height: 250px;
    border-radius: 50%;
    background: var(--faint-grey);
    opacity: 0.7;
  }
  .contact-list {
    position: absolute;
    left: 34px;
    top: 128px;
    list-style: none;
    font-size: 14.5px;
    color: var(--text-dark);
    line-height: 1.35;
  }
  .contact-list li {
    display: flex;
    align-items: flex-start;
    gap: 12px;
    margin-bottom: 4px;
  }
  .contact-list svg {
    width: 14px;
    height: 14px;
    flex: none;
    margin-top: 2px;
    fill: var(--icon-grey);
  }
  .contact-list .web { color: var(--brand-blue); }
</style>
</head>
<body>
<main class="canvas">
  <section class="card card-back" aria-label="Card back">
    <span class="brand-dot"></span>
    <span class="brand-name">Morgan Halberd</span>
  </section>

  <section class="card card-front" aria-label="Card front">
    <div class="faint-disc"></div>
    <div class="brand">
      <span class="brand-dot"></span>
      <span class="brand-name">Morgan Halberd</span>
    </div>
    <ul class="contact-list">
      <li>
        <svg viewBox="0 0 16 16" aria-hidden="true"><circle cx="8" cy="5" r="3.5"/><path d="M1 16c0-4 3-6.5 7-6.5s7 2.5 7 6.5z"/></svg>
        <span>+61 400 555 917<br>+1 555 208 4471</span>
      </li>
      <li>
        <svg viewBox="0 0 16 16" aria-hidden="true"><circle cx="8" cy="8" r="7" fill="none" stroke="#6a6a6e" stroke-width="1.6"/><path d="M1 8h14M8 1c-3 3.5-3 10.5 0 14M8 1c3 3.5 3 10.5 0 14" fill="none" stroke="#6a6a6e" stroke-width="1.2"/></svg>
        <span class="web">www.morganhalberd-example.com</span>
      </li>
      <li>
        <svg viewBox="0 0 16 16" aria-hidden="true"><rect x="0.5" y="3" width="15" height="10" rx="1"/><path d="M1 3.5l7 5 7-5" fill="none" stroke="#fff" stroke-width="1.3"/></svg>
        <span>morgan@morganhalberd-example.com</span>
      </li>
    </ul>
  </section>
</main>
</body>
</html>
```